Lanternfield Billboard - Financial Services Company (Investments, Tax Planning and Insurance)

Our new office has a billboard directly above the office building. We'd like something eye-catching with a strong Call to Action, with the main part of the billboard being under 7 words if possible. We'd like you to include a way to get ahold of us (either our website lanternfieldllc.example or our phone number 302-418-2967. You may also include in small font something to indicate that we've been serving the area since 1980 (the DE area, the tri-state area, the Copperleaf Basin, etc.)

We offer financial planning, tax planning, and insurance, and we help our clients to focus on their goals and happiness by providing everything they need for lifelong wealth under one roof.

Our logos are attached, we use a triangle logo with green and gray. We use the tagline "experience lifelong wealth" but this does not need to be included.

Potential ideas we have seen from other financial companies-
- the concept that the driver spends more time looking at billboards than planning for their retirement
-something along the lines of "everything you need for your finances is in this building right here" planning, investments, taxes, insurance"
-don't spend your time worrying about retirement, let us help you plan for it
-are you working for your money, or is it working for you?
- retirement takes planning, we're here to help
- ready to retire? talk to us
- need investment advice?
- need help investing?
- crossing your fingers isn't a retirement plan. we can help.
- retiring soon? you need help.

Those are just general ideas, please feel free to be creative.

brand colors:
#00b585
#00b185
#000000
#ffffff
#6d6f75
#6d6f75
#6f7074
#021712
#052e24

```html
<!DOCTYPE html>
<html lang="en">
<head>
<meta charset="utf-8">
<title>Lanternfield Billboard</title>
<link href="https://fonts.googleapis.com/css2?family=Poppins:wght@600;700;800&display=swap" rel="stylesheet">
<style>
  :root {
    --brand-green: #00b585;
    --deep-green: #052e24;
    --ink: #021712;
    --black: #000000;
    --white: #ffffff;
    --steel: #6d6f75;
    --canvas: #ffffff;
  }
  * { margin: 0; padding: 0; box-sizing: border-box; }
  html, body {
    width: 1199px;
    height: 1200px;
    overflow: hidden;
    background: var(--canvas);
    font-family: "Poppins", sans-serif;
  }
  .billboard {
    position: absolute;
    left: 50px;
    top: 440px;
    width: 1100px;
    height: 321px;
    box-shadow: 0 10px 22px rgba(0, 0, 0, 0.18);
    display: flex;
    flex-direction: column;
  }
  .headline-band {
    height: 120px;
    background: var(--deep-green);
    display: flex;
    align-items: center;
    justify-content: center;
  }
  .headline {
    color: var(--white);
    font-weight: 800;
    font-size: 73px;
    letter-spacing: -0.5px;
    line-height: 1;
    padding-top: 6px;
  }
  .services-band {
    height: 48px;
    background: var(--brand-green);
    display: flex;
    align-items: center;
    justify-content: space-between;
    padding: 0 46px 0 40px;
  }
  .service {
    display: flex;
    align-items: center;
    gap: 14px;
    color: var(--white);
    font-weight: 700;
    font-size: 31px;
    line-height: 1;
  }
  .service svg { width: 25px; height: 25px; flex: none; }
  .info-panel {
    height: 142px;
    background: var(--white);
    display: flex;
    align-items: center;
    padding: 0 46px 0 48px;
  }
  .brand-block {
    width: 340px;
    display: flex;
    flex-direction: column;
    gap: 14px;
  }
  .brand-name {
    display: flex;
    align-items: center;
    gap: 14px;
    color: var(--brand-green);
    font-weight: 700;
    font-size: 46px;
    line-height: 1;
  }
  .brand-mark {
    width: 34px;
    height: 34px;
    background: var(--brand-green);
    flex: none;
  }
  .website {
    font-weight: 700;
    font-size: 19px;
    color: var(--black);
    letter-spacing: -0.2px;
    white-space: nowrap;
  }
  .website .domain { color: var(--brand-green); }
  .contact-block {
    margin-left: auto;
    display: flex;
    flex-direction: column;
    align-items: flex-end;
  }
  .since-line {
    font-weight: 700;
    font-size: 26px;
    color: var(--black);
    letter-spacing: -0.4px;
    line-height: 1.1;
  }
  .phone {
    display: flex;
    align-items: center;
    gap: 14px;
    color: var(--ink);
    font-weight: 700;
    font-size: 80px;
    line-height: 1;
    letter-spacing: 1px;
    margin-top: 4px;
  }
  .phone svg { width: 30px; height: 62px; flex: none; }
  .base-strip {
    height: 11px;
    background: var(--steel);
  }
</style>
</head>
<body>
  <section class="billboard">
    <header class="headline-band">
      <h1 class="headline">NEED INVESTMENT ADVICE?</h1>
    </header>

    <ul class="services-band">
      <li class="service">
        <svg viewBox="0 0 24 24" aria-hidden="true"><rect x="2" y="2" width="20" height="20" rx="3.5" fill="none" stroke="#021712" stroke-width="2.6"/><path d="M7.5 12.5l3 3 6-6.5" fill="none" stroke="#021712" stroke-width="2.4" stroke-linecap="round" stroke-linejoin="round"/></svg>
        PLANNING
      </li>
      <li class="service">
        <svg viewBox="0 0 24 24" aria-hidden="true"><rect x="2" y="2" width="20" height="20" rx="3.5" fill="none" stroke="#021712" stroke-width="2.6"/><path d="M7.5 12.5l3 3 6-6.5" fill="none" stroke="#021712" stroke-width="2.4" stroke-linecap="round" stroke-linejoin="round"/></svg>
        INVESTMENTS
      </li>
      <li class="service">
        <svg viewBox="0 0 24 24" aria-hidden="true"><rect x="2" y="2" width="20" height="20" rx="3.5" fill="none" stroke="#021712" stroke-width="2.6"/><path d="M7.5 12.5l3 3 6-6.5" fill="none" stroke="#021712" stroke-width="2.4" stroke-linecap="round" stroke-linejoin="round"/></svg>
        TAXES
      </li>
      <li class="service">
        <svg viewBox="0 0 24 24" aria-hidden="true"><rect x="2" y="2" width="20" height="20" rx="3.5" fill="none" stroke="#021712" stroke-width="2.6"/><path d="M7.5 12.5l3 3 6-6.5" fill="none" stroke="#021712" stroke-width="2.4" stroke-linecap="round" stroke-linejoin="round"/></svg>
        INSURANCE
      </li>
    </ul>

    <div class="info-panel">
      <div class="brand-block">
        <div class="brand-name"><span class="brand-mark"></span>Lanternfield</div>
        <div class="website">WWW.<span class="domain">LANTERNFIELDLLC</span>.EXAMPLE</div>
      </div>
      <div class="contact-block">
        <p class="since-line">WE'VE BEEN SERVING THE AREA SINCE 1980</p>
        <p class="phone">
          <svg viewBox="0 0 30 62" aria-hidden="true"><path d="M20 3c-9 4-16 14-16 28s7 24 16 28l6-3c1-1 1-2 0-3l-5-10c-1-1-2-1-3-1l-3 1c-2-3-3-8-3-12s1-9 3-12l3 1c1 0 2 0 3-1l5-10c1-1 1-2 0-3z" fill="#00b585" stroke="#021712" stroke-width="2.5" stroke-linejoin="round"/></svg>
          302-418-2967
        </p>
      </div>
    </div>

    <div class="base-strip"></div>
  </section>
</body>
</html>
```